Venture Capital firm needs modern business cards

We are a Venture Capital firm within financial services/Asset management. The industry generally has basic business cards with black, blue and maybe green/yellow design elements.
Our firm has a four-colour swoosh logo. We are based in London and want to stand out, just a little bit!, from the crowd. Our company is called ROLK Investments and the 'C' stands for collaboration thus using artfolkhub is a natural portal for our business card design competition. Our logo came via artfolkhub too!
We use 'Venture Partner in Asset Management' as our tagline and this is Trademark registered. We operate in a conservative industry and we should not overstep our mark. The logo is colorful as it is and therefore the rest of the design should not be too fanciful.
The objective is twofold: make our logo element stick and memorable with our audience, whilst representing a conservative yet young image.
The Business Card obviously needs a field for Name, Surname, Job Title, Adress fields: Street, City, Postcode, Country, telefone and cell number, website address, etc.
We have uploaded the ai file. We trust that these are OK. If not, please advise.
Reason: We have have been busy with a client engagement. We will set the project as Guaranteed in return for the troubles we cause. Apologies for the confusion.
Thank you all for these great and creative design suggestions. The team is very happy with a number of your ideas! We will be in touch tomorrow to give individual feedback before the project closes on Friday. We look forward to working with some of you to narrow down your creations. Thank you, ROLK Investments team.
All,
Target Market(s)
Financial Services Professionals, Investors, Media, 35-70 years, mainly male, well educated
Industry/Entity Type
Conservative
Requirements
Must have
- We must make use of our logo and potential tagline 'Venture Partner in Asset Management' as we are establishing a new Brand and new company in the market.
We can use 'ROLK', 'ROLK Investments', and 'ROLK Investments'+tagline 'Venture Partner in Asset Management' or simply the four-colour swoosh plus the name of the company as part of the text. (see files)
All design elements are available in black or grey-scale if required. (grey scale swoosh attached).
Due to regulation we must have the following wording on the card in small print 'ROLK Investments is an Appointed Representative of Brambury Monetary Ventures Limited, which is authorised by the Pemberton Oversight Board'.
Nice to have
- We would consider designs that make use of different printing techniques such embossing/debossing, UV spot etc.
We attach our colour palette in the files section for your reference.
Should not have
- The font we use for our company name is 'EXO' so do not use a font style that clashes with the corporate fonts, please.
Do not use other design elements than the ones we provide in the file library as part of this project.

```html
<!DOCTYPE html>
<html lang="en">
<head>
<meta charset="utf-8">
<title>ROLK Investments – Business Card</title>
<link rel="stylesheet" href="https://fonts.googleapis.com/css2?family=Barlow:wght@300;400;500&display=swap">
<style>
  :root {
    --backdrop: #9a9a9a;
    --card: #ffffff;
    --ink-name: #6d6e71;
    --ink-body: #6a6a6a;
    --ink-brand: #4a4b4d;
    --accent: #8cc63f;
    --pattern: #e6e6e6;
    --pattern-soft: #f3f3f3;
  }
  * { margin: 0; padding: 0; box-sizing: border-box; }
  html, body { width: 1200px; height: 487px; overflow: hidden; }
  body {
    background: var(--backdrop);
    font-family: "Barlow", Arial, sans-serif;
    position: relative;
  }
  .card {
    position: absolute;
    top: 80px;
    width: 532px;
    height: 326px;
    background: var(--card);
    overflow: hidden;
  }
  .card--front { left: 53px; }
  .card--back { left: 607px; }

  /* Cardholder */
  .holder { position: absolute; left: 214px; top: 26px; }
  .holder__name {
    font-size: 18px; font-weight: 400; color: var(--ink-name);
    letter-spacing: 0.2px; line-height: 22px;
  }
  .holder__title {
    font-size: 14px; font-weight: 400; color: var(--accent); line-height: 20px;
  }

  /* Brand block */
  .brand__dot {
    position: absolute; left: 106px; top: 96px;
    width: 92px; height: 92px; border-radius: 50%; background: var(--accent);
  }
  .brand__name {
    position: absolute; left: 214px; top: 86px;
    color: var(--ink-brand); font-weight: 400;
  }
  .brand__word {
    display: block; font-size: 90px; line-height: 90px; letter-spacing: 1px;
  }
  .brand__sub {
    display: block; font-size: 18px; line-height: 20px; letter-spacing: 10.2px;
    margin-top: 2px; padding-left: 3px;
  }

  /* Contact details */
  .contact {
    position: absolute; left: 197px; top: 227px;
    list-style: none;
    font-size: 13.5px; font-weight: 300; color: var(--ink-body);
    line-height: 17.5px;
  }
  .contact__row { display: flex; align-items: flex-start; gap: 6px; }
  .contact__icon { width: 11px; height: 11px; margin-top: 3px; flex: none; fill: var(--accent); }
  .contact__pair { display: inline-flex; align-items: flex-start; gap: 6px; margin-left: 24px; }
  .contact__web strong { color: var(--accent); font-weight: 500; }

  /* Back */
  .back-field {
    position: absolute; left: 12px; top: 12px; right: 12px; bottom: 12px;
    background: radial-gradient(circle at 50% 50%, var(--pattern-soft), var(--pattern));
  }
  .back-mark {
    position: absolute; left: 404px; top: 214px;
    display: flex; align-items: center; gap: 5px;
    background: var(--card); padding: 6px 6px;
  }
  .back-mark__dot { width: 10px; height: 10px; border-radius: 50%; background: var(--accent); }
  .back-mark__name { font-size: 15px; font-weight: 400; color: var(--ink-brand); line-height: 1; }
</style>
</head>
<body>
  <section class="card card--front" aria-label="Business card front">
    <div class="holder">
      <p class="holder__name">CARDHOLDER NAME</p>
      <p class="holder__title">Designation</p>
    </div>

    <span class="brand__dot"></span>
    <p class="brand__name">
      <span class="brand__word">ROLK</span>
      <span class="brand__sub">Investments</span>
    </p>

    <ul class="contact">
      <li class="contact__row">
        <svg class="contact__icon" viewBox="0 0 12 12"><path d="M6 0a4 4 0 0 0-4 4c0 3 4 8 4 8s4-5 4-8a4 4 0 0 0-4-4zm0 5.5A1.5 1.5 0 1 1 6 2.5a1.5 1.5 0 0 1 0 3z"/></svg>
        <span>0101 Sunset Avenue, Suite No. 123,<br>Your City, City Code, Your Country</span>
      </li>
      <li class="contact__row">
        <svg class="contact__icon" viewBox="0 0 12 12"><circle cx="6" cy="6" r="6"/><path d="M4 3l1 2-1 1c.5 1 1 1.5 2 2l1-1 2 1-.5 1.5C6 9.5 2.5 6 2.5 3.5z" fill="#fff"/></svg>
        <span>+012 345 6789</span>
        <span class="contact__pair">
          <svg class="contact__icon" viewBox="0 0 12 12"><rect x="3" y="0" width="6" height="4"/><rect x="0" y="5" width="12" height="7" rx="1"/></svg>
          <span>+012 345 6780</span>
        </span>
      </li>
      <li class="contact__row">
        <svg class="contact__icon" viewBox="0 0 12 12"><rect x="0" y="2" width="12" height="8" rx="1"/><path d="M2 4h8M2 6h8M3 8h6" stroke="#fff" stroke-width="0.8"/></svg>
        <span>cardholder.name@rolkinvestments.com</span>
      </li>
      <li class="contact__row">
        <svg class="contact__icon" viewBox="0 0 12 12"><circle cx="6" cy="6" r="6"/><path d="M0 6h12M6 0c-2.5 3-2.5 9 0 12M6 0c2.5 3 2.5 9 0 12" stroke="#fff" stroke-width="0.8" fill="none"/></svg>
        <span class="contact__web">www.<strong>rolkinvestments</strong>.com</span>
      </li>
    </ul>
  </section>

  <section class="card card--back" aria-label="Business card back">
    <div class="back-field" role="img" aria-label="Repeating pale grey brand pattern covering the card back"></div>
    <div class="back-mark">
      <span class="back-mark__dot"></span>
      <span class="back-mark__name">ROLK</span>
    </div>
  </section>
</body>
</html>
```